Progressive/contemporary business card design for successful Startups as a Service Company

New logo launched in 2020. New website launched in 2021. Now that COVID is (mostly) behind us, I'm networking with more people and need a business card that matches the company/logo design aesthetic.

```html
<!DOCTYPE html>
<html lang="en">
<head>
<meta charset="utf-8">
<title>Brightpath Business Card</title>
<link href="https://fonts.googleapis.com/css2?family=Montserrat:wght@300;400;500;700&display=swap" rel="stylesheet">
<style>
  :root {
    --stage: #d9d9db;
    --card: #2a2a2c;
    --white: #f4f4f4;
    --text-light: #f2f2f2;
    --text-muted: #8d8d90;
    --band-text: #6e6e72;
    --band-strong: #2c3550;
    --corner-grey: #8e8e90;
    --silver: #bdbdc0;
    --blue: #1b9be0;
    --orange: #f28a1a;
    --green: #6cbf3a;
    --magenta: #d61f8c;
  }
  * { margin: 0; padding: 0; box-sizing: border-box; }
  html, body { width: 1200px; height: 800px; overflow: hidden; }
  body {
    background: var(--stage);
    font-family: "Montserrat", sans-serif;
    display: flex;
    align-items: center;
    justify-content: center;
    gap: 40px;
  }
  .card {
    position: relative;
    width: 540px;
    height: 309px;
    background: var(--card);
    overflow: hidden;
    box-shadow: 0 10px 24px rgba(0,0,0,0.18);
  }

  /* Contact side */
  .identity {
    position: absolute;
    right: 290px;
    top: 118px;
    text-align: right;
  }
  .identity__name {
    color: var(--text-light);
    font-weight: 700;
    font-size: 19px;
    letter-spacing: 0.5px;
    white-space: nowrap;
  }
  .identity__title {
    color: var(--text-muted);
    font-weight: 400;
    font-size: 12px;
    letter-spacing: 0.6px;
    margin-top: 2px;
  }
  .divider {
    position: absolute;
    left: 268px;
    top: 92px;
    width: 2px;
    height: 92px;
    display: flex;
    flex-direction: column;
  }
  .divider span { flex: 1; }
  .divider .d1 { background: var(--blue); }
  .divider .d2 { background: var(--orange); }
  .divider .d3 { background: var(--green); }
  .divider .d4 { background: var(--magenta); }

  .contact {
    position: absolute;
    left: 290px;
    top: 52px;
    list-style: none;
    color: var(--text-light);
    font-size: 10.5px;
    line-height: 15px;
    font-weight: 400;
  }
  .contact li {
    display: flex;
    align-items: flex-start;
    gap: 8px;
  }
  .contact li + li { margin-top: 2px; }
  .contact .address { margin-bottom: 6px; }
  .contact svg {
    width: 10px;
    height: 10px;
    margin-top: 2px;
    flex: none;
    fill: var(--text-muted);
  }

  .web-band {
    position: absolute;
    left: 0;
    top: 248px;
    width: 448px;
    height: 30px;
    background: var(--white);
    display: flex;
    align-items: center;
    padding-left: 214px;
    font-size: 11px;
    letter-spacing: 1.4px;
    color: var(--band-text);
  }
  .web-band strong { color: var(--band-strong); font-weight: 700; }
  .brand-square {
    position: absolute;
    left: 462px;
    top: 222px;
    width: 26px;
    height: 26px;
    background: var(--magenta);
  }
  .corner-block {
    position: absolute;
    right: 0;
    top: 198px;
    width: 36px;
    height: 36px;
    background: var(--corner-grey);
  }

  /* Brand side */
  .wordmark {
    position: absolute;
    left: 50%;
    top: 50%;
    transform: translate(-50%, -50%);
    display: flex;
    align-items: center;
    gap: 16px;
  }
  .wordmark__name {
    color: var(--silver);
    font-weight: 400;
    font-size: 34px;
    letter-spacing: 8px;
    white-space: nowrap;
  }
  .wordmark__square {
    width: 30px;
    height: 30px;
    background: var(--blue);
  }
</style>
</head>
<body>

  <section class="card card--contact">
    <div class="identity">
      <p class="identity__name">DANIEL REYES</p>
      <p class="identity__title">President</p>
    </div>

    <div class="divider" aria-hidden="true">
      <span class="d1"></span><span class="d2"></span><span class="d3"></span><span class="d4"></span>
    </div>

    <ul class="contact">
      <li class="address">
        <svg viewBox="0 0 10 10" aria-hidden="true"><path d="M5 0a3.4 3.4 0 0 0-3.4 3.4C1.6 6 5 10 5 10s3.4-4 3.4-6.6A3.4 3.4 0 0 0 5 0zm0 4.8a1.4 1.4 0 1 1 0-2.8 1.4 1.4 0 0 1 0 2.8z"/></svg>
        <span>412 Cedar Hollow Road<br>Harbor Point, Alaska 99611</span>
      </li>
      <li>
        <svg viewBox="0 0 10 10" aria-hidden="true"><path d="M2 0.5l1.8 2.2-1 1.2a6 6 0 0 0 3.3 3.3l1.2-1L9.5 8 8.3 9.5C4.2 9.2 0.8 5.8 0.5 1.7z"/></svg>
        <span>555-201-4418</span>
      </li>
      <li>
        <svg viewBox="0 0 10 10" aria-hidden="true"><path d="M0.5 2h9v6h-9zM1.5 3v4h7V3z"/></svg>
        <span>555-307-2269</span>
      </li>
      <li>
        <svg viewBox="0 0 10 10" aria-hidden="true"><path d="M3 0h4v10H3zM3.8 1v7h2.4V1z"/></svg>
        <span>555-419-8830</span>
      </li>
      <li>
        <svg viewBox="0 0 10 10" aria-hidden="true"><path d="M0.5 2h9v6.5h-9zM1.4 2.8L5 5.6l3.6-2.8z"/></svg>
        <span>daniel@brightpath.com</span>
      </li>
    </ul>

    <div class="web-band">www.<strong>BRIGHTPATH</strong>.com</div>
    <div class="brand-square" aria-hidden="true"></div>
    <div class="corner-block" aria-hidden="true"></div>
  </section>

  <section class="card card--brand">
    <div class="wordmark">
      <span class="wordmark__name">BRIGHTPATH</span>
      <span class="wordmark__square" aria-hidden="true"></span>
    </div>
  </section>

</body>
</html>
```